Presentation card Venture KELO - Tech Incubator from Perú

We need a Design to promote the incubator of technology Startups.
We are in Perú, we work with a string tech filter and develop enterprenurship competencies in the Startup team.
The card is to facilitators and staff memebers of VentureKELO.
We want a clear, modern, tech and agile Design.

We work to help New enterprises of technology here in Perú, we expect the candidates have a big competencies to Research and develop technological products.

We work using methodologies from QRB, Folmestry, Brakewell and Harrowgate univeesities. Our book base is the disciplina of enterpreneur.

We work events all year using diferent formats: Brightforge, Vorne price, OPRA Model Competition you can use these logros in your Design.

Set the name, role, email, cell phone number, address.

Example:
// Contact info section
Tobías Quiroveda
Swift Modeling Hub Manager
tobias.quiroveda@kelo-example.pe
(511) 999 000 417

// Address info section
VentureKELO
Technology-based business incubator
Av. Los Cedrales 884, Valdora
Lima - Perú
web: venture-kelo-example.org.pe
email: venture@kelo-example.pe
phone number: (511) 3926508 ext. 4418

// (optional)Lema section
Making happy using technology

// Social network section
facebook: venturekelooficial

Target Market(s)

Enterprenurship, CTO, Investors, Companies interested on open innovation services

Industry/Entity Type

Information Technology

Contact Information for Business Card

Name, Role, Email, Cell phone number

Colors

Designer to choose colors to be used in the design.

Requirements
Must have
• Logo forms and colors
Nice to have
• I add pictures of the leaders of incubator
Should not have
• No vertical designs

```html
<!DOCTYPE html>
<html lang="en">
<head>
<meta charset="utf-8">
<title>Venture KELO – Business Card</title>
<link rel="stylesheet" href="https://fonts.googleapis.com/css2?family=Montserrat:wght@700;800&family=Arimo:wght@400;700&display=swap">
<style>
  :root {
    --stage: #1c1c1c;
    --card-back: #121212;
    --card-front: #242424;
    --ink-white: #f4f4f4;
    --ink-grey: #a9a9a9;
    --accent: #c63a63;
    --divider: #5a5a5a;
  }
  html, body {
    margin: 0;
    padding: 0;
    width: 1200px;
    height: 1200px;
    overflow: hidden;
    background: var(--stage);
  }
  .canvas {
    position: relative;
    width: 1200px;
    height: 1200px;
    display: flex;
    flex-direction: column;
    align-items: center;
    justify-content: center;
    gap: 60px;
  }
  .card {
    position: relative;
    width: 860px;
    height: 491px;
    border-radius: 26px;
    box-sizing: border-box;
    overflow: hidden;
  }
  /* Back side */
  .card--back {
    background: var(--card-back);
    display: flex;
    flex-direction: column;
    align-items: center;
    justify-content: center;
    gap: 44px;
  }
  .brand {
    display: flex;
    align-items: center;
    gap: 14px;
    font-family: "Montserrat", sans-serif;
    font-weight: 800;
    color: var(--ink-white);
    text-transform: uppercase;
    line-height: 1;
  }
  .brand__mark {
    background: var(--accent);
    display: block;
  }
  .card--back .brand { font-size: 54px; }
  .card--back .brand__mark { width: 34px; height: 34px; background: var(--ink-white); }
  .tagline {
    margin: 0;
    width: 560px;
    text-align: center;
    font-family: "Arimo", sans-serif;
    font-weight: 700;
    font-size: 17px;
    line-height: 1.45;
    color: var(--ink-grey);
  }
  /* Front side */
  .card--front {
    background: var(--card-front);
    display: flex;
    align-items: center;
    padding: 0 60px 40px 70px;
  }
  .pattern-fill {
    position: absolute;
    inset: 0;
    background: linear-gradient(135deg, #272727, #202020);
  }
  .front-layout {
    position: relative;
    display: flex;
    align-items: center;
    gap: 34px;
  }
  .card--front .brand { font-size: 40px; }
  .card--front .brand__mark { width: 26px; height: 26px; }
  .divider {
    width: 1px;
    height: 130px;
    background: var(--divider);
  }
  .contact { font-family: "Arimo", sans-serif; }
  .contact__name {
    margin: 0;
    font-family: "Montserrat", sans-serif;
    font-weight: 800;
    font-size: 27px;
    color: var(--ink-white);
    text-transform: uppercase;
    letter-spacing: 0.5px;
  }
  .contact__role {
    margin: 2px 0 18px;
    font-size: 19px;
    color: var(--accent);
    text-transform: uppercase;
    letter-spacing: 0.5px;
  }
  .contact__line {
    display: flex;
    align-items: center;
    gap: 14px;
    margin: 6px 0;
    font-size: 19px;
    color: var(--ink-white);
  }
  .contact__icon { width: 22px; height: 22px; flex: none; }
</style>
</head>
<body>
<main class="canvas">
  <section class="card card--back" aria-label="Card back">
    <div class="brand"><span class="brand__mark"></span><span>Venture KELO</span></div>
    <p class="tagline">We work to help new enterprises of technology here in Perú, we expect the candidates have a big competencies to Research and develop technological products.</p>
  </section>

  <section class="card card--front" aria-label="Card front">
    <div class="pattern-fill" role="img" aria-label="Subtle dark interlocking geometric pattern"></div>
    <div class="front-layout">
      <div class="brand"><span class="brand__mark"></span><span>Venture KELO</span></div>
      <div class="divider"></div>
      <div class="contact">
        <p class="contact__name">Tobías Quiroveda</p>
        <p class="contact__role">Swift Modeling Hub Manager</p>
        <div class="contact__line">
          <svg class="contact__icon" viewBox="0 0 24 24" fill="none" stroke="var(--accent)" stroke-width="2">
            <rect x="6" y="2" width="12" height="20" rx="2"/>
            <line x1="10" y1="18" x2="14" y2="18"/>
          </svg>
          <span>555.014.2290</span>
        </div>
        <div class="contact__line">
          <svg class="contact__icon" viewBox="0 0 24 24">
            <rect x="2" y="5" width="20" height="14" fill="var(--accent)"/>
            <polyline points="2,5 12,13 22,5" fill="none" stroke="var(--card-front)" stroke-width="1.6"/>
          </svg>
          <span>tobiasquiroveda@venturekelo-example.com</span>
        </div>
      </div>
    </div>
  </section>
</main>
</body>
</html>
```